Billboard design for agricultural machinery business

hello im looking for roadside advertiement sign to be designed, the sign is 10ft up in the air and is 4ft high and 8ft wide, id image i like a blue background and my logo front and centre and below logo sales - service - parts and then below that the brook meadow symbol and tull symbol, I’d also like the website www.Ploverfield.ie on it. i am open to suggestions and designs. blue is #005999 and yellow is rgb (254, 205, 26) ive attached my log and symbols, im open to different colour backgrounds or just white and also open to brook meadow and tull as writhing rather than logos

Target Market(s)

Brook Meadow and tull tractor owners

Industry/Entity Type

Agricultural machine sales service and parts

Colors

Designer to choose colors to be used in the design.

Requirements
Must have
• My logo and colours, brands brook Meadow and tull, website

```html
<!DOCTYPE html>
<html lang="en">
<head>
<meta charset="utf-8">
<title>Ploverfield Roadside Billboard</title>
<link rel="stylesheet" href="https://fonts.googleapis.com/css2?family=Fredoka:wght@500;600;700&display=swap">
<style>
  :root {
    --brand-blue: #005999;
    --field-blue-dark: #0a4f86;
    --field-blue-light: #1f6aa6;
    --brand-yellow: rgb(254, 205, 26);
    --band-yellow: #ecc53f;
    --white: #ffffff;
    --stage: #dfe6ec;
  }
  * { box-sizing: border-box; margin: 0; padding: 0; }
  html, body {
    width: 1200px;
    height: 900px;
    overflow: hidden;
    background: var(--stage);
    font-family: "Fredoka", Arial, sans-serif;
  }
  .billboard {
    position: absolute;
    left: 50px;
    top: 175px;
    width: 1100px;
    height: 550px;
    background: var(--brand-blue);
    overflow: hidden;
  }
  .field-backdrop {
    position: absolute;
    inset: 0;
    background:
      radial-gradient(ellipse at 55% 0%, var(--field-blue-light) 0%, transparent 60%),
      linear-gradient(180deg, var(--field-blue-dark), var(--brand-blue) 55%, var(--field-blue-dark));
  }
  .brand-mark {
    position: absolute;
    top: 85px;
    left: 0;
    right: 0;
    display: flex;
    justify-content: center;
    align-items: center;
    gap: 18px;
  }
  .brand-mark__dot {
    width: 34px;
    height: 34px;
    border-radius: 50%;
    background: var(--brand-yellow);
  }
  .brand-mark__name {
    color: var(--white);
    font-weight: 600;
    font-size: 78px;
    line-height: 1;
  }
  .services-band {
    position: absolute;
    left: 0;
    right: 0;
    top: 235px;
    height: 110px;
    background: var(--band-yellow);
    display: flex;
    align-items: center;
    justify-content: center;
  }
  .services-band__text {
    color: var(--brand-blue);
    font-weight: 700;
    font-size: 88px;
    letter-spacing: 1px;
    line-height: 1;
    white-space: nowrap;
  }
  .footer-row {
    position: absolute;
    left: 55px;
    right: 45px;
    top: 400px;
    height: 80px;
    display: flex;
    align-items: center;
    white-space: nowrap;
  }
  .dealer-brand {
    color: var(--white);
    font-weight: 600;
    font-size: 40px;
    line-height: 1;
    margin-right: 36px;
  }
  .contact-web {
    margin-left: auto;
    display: flex;
    align-items: center;
    gap: 16px;
  }
  .contact-web__icon { width: 48px; height: 48px; flex: none; }
  .contact-web__address {
    color: var(--white);
    font-weight: 600;
    font-size: 50px;
    letter-spacing: 1px;
    line-height: 1;
  }
</style>
</head>
<body>
  <main class="billboard">
    <div class="field-backdrop" role="img" aria-label="Blue-toned photograph of crop rows stretching toward the horizon"></div>

    <div class="brand-mark">
      <span class="brand-mark__name">Ploverfield</span>
      <span class="brand-mark__dot"></span>
    </div>

    <div class="services-band">
      <p class="services-band__text">SALES - SERVICE - PARTS</p>
    </div>

    <div class="footer-row">
      <span class="dealer-brand">Brook Meadow</span>
      <span class="dealer-brand">Tull</span>
      <div class="contact-web">
        <svg class="contact-web__icon" viewBox="0 0 50 50" aria-hidden="true">
          <circle cx="25" cy="25" r="25" fill="var(--band-yellow)"/>
          <g fill="none" stroke="var(--brand-blue)" stroke-width="2.6">
            <circle cx="25" cy="25" r="13"/>
            <ellipse cx="25" cy="25" rx="6" ry="13"/>
            <line x1="12" y1="25" x2="38" y2="25"/>
          </g>
        </svg>
        <span class="contact-web__address">www.Ploverfield.ie</span>
      </div>
    </div>
  </main>
</body>
</html>
```